New Business Card Design Project

Use the flyer uploaded and website www.brightoakbuilders.com for inspiration.
List Our Services on Backside of business cards
Martin Hollis
Harborline Renovations Inc.
Licensed General Contractors
858-471-9063

Contact Information for Business Card

Use the flyer uploaded and website www.brightoakbuilders.com for inspiration. List Our Services on Backside of business cards Martin Hollis Harborline Renovations Inc. Licensed General Contractors 858-471-9063

```html
<!DOCTYPE html>
<html lang="en">
<head>
<meta charset="utf-8">
<title>Harborline Renovations – Business Card</title>
<link rel="stylesheet" href="https://fonts.googleapis.com/css2?family=Poppins:wght@300;400;500;600;700&display=swap">
<style>
  :root {
    --page-bg: #ececec;
    --card-bg: #2b2b2c;
    --ink: #ffffff;
    --ink-muted: #8e8e8e;
    --portrait-fill: #d9d9d9;
  }
  * { box-sizing: border-box; margin: 0; padding: 0; }
  html, body {
    width: 1200px; height: 1200px; overflow: hidden;
    background: var(--page-bg);
    font-family: "Poppins", sans-serif;
  }
  .canvas {
    width: 1200px; height: 1200px;
    display: flex; flex-direction: column;
    align-items: center; justify-content: center; gap: 60px;
  }
  .card {
    position: relative;
    width: 760px; height: 434px;
    background: var(--card-bg);
    border-radius: 30px;
    color: var(--ink);
    box-shadow: 0 10px 30px rgba(0,0,0,0.15);
  }

  /* Front */
  .portrait-frame {
    position: absolute; left: 56px; top: 70px;
    width: 230px; height: 230px;
    border-radius: 50%;
    border: 7px solid var(--ink);
    padding: 10px;
  }
  .portrait-area {
    width: 100%; height: 100%; border-radius: 50%;
    background: var(--portrait-fill);
  }
  .contact {
    position: absolute; left: 320px; top: 170px;
  }
  .contact-name { font-size: 34px; font-weight: 600; line-height: 1.15; }
  .contact-title { font-size: 21px; font-weight: 400; color: var(--ink-muted); margin-bottom: 4px; }
  .contact-line { font-size: 22px; font-weight: 300; line-height: 1.3; }
  .website {
    position: absolute; left: 56px; bottom: 40px;
    font-size: 20px; font-weight: 300; color: var(--ink-muted);
  }
  .brand-mark {
    display: flex; align-items: center; gap: 8px;
    font-weight: 400; letter-spacing: 0.08em; text-transform: uppercase;
    color: var(--ink);
  }
  .brand-mark .brand-square {
    border: 1.5px solid var(--ink);
  }
  .front-brand {
    position: absolute; right: 40px; top: 48px; font-size: 12px;
  }
  .front-brand .brand-square { width: 16px; height: 16px; }

  /* Back */
  .back-brand {
    position: absolute; left: 50px; top: 190px; font-size: 20px; gap: 12px;
  }
  .back-brand .brand-square { width: 30px; height: 30px; }
  .services {
    position: absolute; left: 430px; top: 70px;
  }
  .services-title { font-size: 28px; font-weight: 600; margin-bottom: 8px; }
  .services-list { list-style: none; font-size: 16.5px; font-weight: 300; line-height: 1.42; }
</style>
</head>
<body>
<main class="canvas">
  <section class="card card-front">
    <div class="portrait-frame">
      <div class="portrait-area" role="img" aria-label="Profile silhouette portrait of the contact person"></div>
    </div>
    <div class="brand-mark front-brand"><span class="brand-square"></span>Harborline Renovations</div>
    <div class="contact">
      <p class="contact-name">Martin Hollis</p>
      <p class="contact-title">CEO Business</p>
      <p class="contact-line">Harborline Renovations Inc.</p>
      <p class="contact-line">Licensed General Contractors</p>
      <p class="contact-line">858-471-9063</p>
    </div>
    <p class="website">www.brightoakbuilders.com</p>
  </section>

  <section class="card card-back">
    <div class="brand-mark back-brand"><span class="brand-square"></span>Harborline Renovations</div>
    <div class="services">
      <h2 class="services-title">Our Services :</h2>
      <ul class="services-list">
        <li>Remodel : Kitchen &amp; Bath</li>
        <li>Painting Interior &amp; Exterior</li>
        <li>Flooring : Carpet, Vinyl, Wood</li>
        <li>Window &amp; Door Replacement</li>
        <li>Plumbing : Repairs &amp; Upgrades</li>
        <li>Energy-Efficient Upgrades</li>
        <li>Deck &amp; Patio Construction</li>
        <li>Water &amp; Mold Damage</li>
        <li>Garage Renovation</li>
      </ul>
    </div>
  </section>
</main>
</body>
</html>
```